"Dario Quillon" Business Card

Friends

My name is "Dario Quillon" and I need your help! I need a new business card for my personal use.

As background, "Dario Quillon" is actually an alias that I use when I meet women. Please use your creative skills to create an amazing business card for me to use!

In addition to including my name and contact details (see the "Must Have" section), you may wish to add a catchphrase or a title if you think it would help me :)

For background, please see:

http://www.dailybrightwire.com/2013/07/23/morton-feld-dario-quillon_n_5129847.html

Looking forward to seeing what you can do for me.

Hugs and kisses,

Dario Quillon [courtesy of PixelHarbor]

Target Market(s)

Adult women in New York City...or anywhere really.

Industry/Entity Type

Business

Requirements
Must have
• Please include the following details:

Dario Quillon
P: +1-555-3QUILLN
E: secrets@darioquillon-mail.com
Nice to have
• You might include a catchphrase, like "Quillon is my surname But you can call me Mr Smoothstep".

Or perhaps a title, like "Dario Quillon, Head of Sexy Times".

You're creative...I will leave the details to you my friends.
Should not have
• Any references to my actual name...because then, what's the point in using an alias?

```html
<!DOCTYPE html>
<html lang="en">
<head>
<meta charset="utf-8">
<title>Dario Quillon — Business Card</title>
<link href="https://fonts.googleapis.com/css2?family=Questrial&display=swap" rel="stylesheet">
<style>
  :root {
    --page-bg: #ffffff;
    --card-dark: #0a0a0b;
    --card-mid: #222326;
    --card-light: #46494d;
    --ink: #ffffff;
    --accent: #1aa3d1;
    --shadow: rgba(0, 0, 0, 0.75);
  }
  * { margin: 0; padding: 0; box-sizing: border-box; }
  html, body {
    width: 1200px;
    height: 1000px;
    overflow: hidden;
    background: var(--page-bg);
  }
  .card {
    position: absolute;
    left: 261px;
    top: 315px;
    width: 688px;
    height: 392px;
    background: linear-gradient(90deg, var(--card-dark) 0%, var(--card-mid) 55%, var(--card-light) 100%);
    font-family: "Questrial", "Century Gothic", sans-serif;
    color: var(--ink);
    overflow: hidden;
  }
  .brand-mark {
    position: absolute;
    left: 22px;
    top: 76px;
    display: flex;
    align-items: center;
    gap: 10px;
  }
  .brand-mark__dot {
    width: 18px;
    height: 18px;
    border-radius: 50%;
    background: var(--accent);
  }
  .brand-mark__name {
    font-size: 26px;
    color: var(--ink);
    line-height: 1;
  }
  .identity {
    position: absolute;
    right: 36px;
    top: 118px;
    text-align: right;
    text-shadow: 2px 2px 4px var(--shadow);
  }
  .identity__name {
    font-size: 52px;
    font-weight: 400;
    line-height: 1;
    letter-spacing: 0.5px;
    word-spacing: 6px;
  }
  .identity__tagline {
    margin-top: 8px;
    margin-right: -3px;
    font-size: 19px;
    line-height: 1;
  }
  .contact {
    position: absolute;
    left: 20px;
    top: 316px;
    list-style: none;
    font-size: 27px;
    line-height: 34px;
    text-shadow: 2px 2px 4px var(--shadow);
  }
</style>
</head>
<body>
  <section class="card" aria-label="Business card for Dario Quillon">
    <div class="brand-mark">
      <span class="brand-mark__dot"></span>
      <span class="brand-mark__name">Quillon</span>
    </div>
    <div class="identity">
      <h1 class="identity__name">Dario Quillon</h1>
      <p class="identity__tagline">Quillon is my surname But you can call me Mr Smoothstep</p>
    </div>
    <ul class="contact">
      <li class="contact__phone">P: +1-555-3QUILLN</li>
      <li class="contact__email">E: secrets@darioquillon-mail.com</li>
    </ul>
  </section>
</body>
</html>
```